Veteran Owned General Contractor needs Bold New Business Cards

We are a service disabled veteran owned small business. We're a general contractor that specializes in excavation, underground utilities, site work, land clearing and demolition. We would like a fresh, simple, bold, new look for our business cards. We're open to ideas! We'd like to incorporate the following information on the card:

Company Name & Logo, Name of Person, Job Title, Office Phone, Fax, Cell Phone, Email Address, Website, SDVOSB

Our logo is included. We look forward to your thoughts.

Thank you!
Updates

Reason: Hello Due to the overwhelming response to this project, we are extending the deadline one time to allow for improved communication and feedback with the top candidates. We would like to thank everyone for their hard work and exceptional creativity! Thank you

Industry/Entity Type

Business

Contact Information for Business Card

Font styles to use
Sans Serif

Requirements
Nice to have
• As we are a veteran owned company, it would be nice to incorporate an American flag into the design. Maybe on the back?

```html
<!DOCTYPE html>
<html lang="en">
<head>
<meta charset="utf-8">
<title>Ironvale Inc – Business Card</title>
<link href="https://fonts.googleapis.com/css2?family=Michroma&family=Roboto+Condensed:wght@500&display=swap" rel="stylesheet">
<style>
  :root {
    --page: #3b3c3e;
    --card-dark: #262627;
    --card-light: #ffffff;
    --green: #5bbf3a;
    --grey: #8c8c8c;
    --grey-light: #b5b5b5;
    --ink: #1c1c1c;
  }
  * { box-sizing: border-box; margin: 0; padding: 0; }
  html, body { width: 1200px; height: 900px; overflow: hidden; background: var(--page); }
  body { position: relative; font-family: "Michroma", sans-serif; }

  .card {
    position: absolute; left: 260px; width: 680px; height: 388px;
    box-shadow: 0 12px 30px rgba(0,0,0,.45); overflow: hidden;
  }

  /* back */
  .card-back { top: 40px; background: var(--card-dark); color: var(--grey-light); }
  .back-brand {
    position: absolute; top: 120px; left: 0; right: 0;
    display: flex; align-items: center; justify-content: center; gap: 18px;
  }
  .brand-square { width: 46px; height: 46px; background: var(--grey); }
  .back-brand .brand-name { font-size: 44px; color: var(--green); letter-spacing: 2px; }
  .specializes {
    position: absolute; top: 210px; left: 0; right: 0; text-align: center;
    font-family: "Roboto Condensed", sans-serif; font-size: 17px; letter-spacing: 1px; color: var(--grey-light);
  }
  .services {
    position: absolute; top: 245px; left: 0; right: 0; text-align: center;
    font-family: "Roboto Condensed", sans-serif; font-size: 14.5px; letter-spacing: .5px; color: var(--grey-light);
  }
  .services .dot {
    display: inline-block; width: 7px; height: 7px; border-radius: 50%;
    background: var(--green); margin: 0 6px; vertical-align: middle;
  }

  /* front */
  .card-front { top: 472px; background: var(--card-light); color: var(--ink); }
  .front-brand { position: absolute; left: 48px; top: 88px; width: 170px; text-align: center; }
  .front-brand .brand-square { width: 130px; height: 130px; margin: 0 auto 16px; background: var(--card-dark); }
  .front-brand .brand-name { font-size: 18px; color: var(--green); letter-spacing: 1px; }
  .divider {
    position: absolute; left: 246px; top: 95px; width: 2px; height: 140px;
    background: linear-gradient(var(--card-light), #555 50%, var(--card-light));
  }
  .contact { position: absolute; left: 276px; top: 92px; }
  .contact-name { font-size: 22px; letter-spacing: 1px; }
  .contact-title { font-size: 13px; color: var(--green); margin: 4px 0 14px; }
  .contact-line { display: flex; align-items: center; gap: 10px; font-size: 13px; line-height: 24px; }
  .contact-line svg { width: 15px; height: 15px; flex: none; }
  .address { position: absolute; left: 48px; bottom: 52px; font-size: 13px; }

  .side-band { position: absolute; top: 0; right: 0; width: 108px; height: 100%; background: var(--card-dark); }
  .side-band::before { content: ""; position: absolute; left: 0; top: 0; width: 12px; height: 100%; background: var(--grey); }
  .side-band .band-name {
    position: absolute; left: 60px; top: 50%;
    transform: translate(-50%, -50%) rotate(-90deg);
    white-space: nowrap; font-size: 36px; color: var(--green); letter-spacing: 1px;
  }
  .side-band .band-suffix { font-size: 14px; color: var(--card-light); margin-left: 8px; }
</style>
</head>
<body>

<section class="card card-back" aria-label="Card back">
  <div class="back-brand">
    <span class="brand-square"></span>
    <span class="brand-name">IRONVALE</span>
  </div>
  <p class="specializes">SPECIALIZES IN</p>
  <p class="services">EXCAVATION<span class="dot"></span>UNDERGROUND UTILITIES<span class="dot"></span>SITE WORK<span class="dot"></span>LAND CLEARING AND DEMOLITION</p>
</section>

<section class="card card-front" aria-label="Card front">
  <div class="front-brand">
    <div class="brand-square"></div>
    <div class="brand-name">IRONVALE</div>
  </div>
  <div class="divider"></div>

  <div class="contact">
    <p class="contact-name">MARCUS HALE</p>
    <p class="contact-title">Managing Director</p>
    <p class="contact-line">
      <svg viewBox="0 0 16 16" fill="none" stroke="#5bbf3a" stroke-width="1.6"><rect x="2" y="3" width="12" height="9" rx="1.5"/><path d="M5 14h6"/></svg>
      0481-226-904
    </p>
    <p class="contact-line">
      <svg viewBox="0 0 16 16" fill="#5bbf3a"><path d="M3.5 1.5l2.5 0 1 3.5-1.6 1.2a8 8 0 0 0 4.4 4.4L11 9l3.5 1v2.5c0 1-1 2-2 2A11 11 0 0 1 1.5 3.5c0-1 1-2 2-2z"/></svg>
      0755-412-390
    </p>
    <p class="contact-line">
      <svg viewBox="0 0 16 16" fill="#5bbf3a"><path d="M1 3h14v10H1z"/><path d="M1 3l7 6 7-6" stroke="#fff" stroke-width="1.3" fill="none"/></svg>
      marcushale@ironvale.com
    </p>
    <p class="contact-line">
      <svg viewBox="0 0 16 16" fill="none" stroke="#5bbf3a" stroke-width="1.4"><circle cx="8" cy="8" r="6.5"/><ellipse cx="8" cy="8" rx="3" ry="6.5"/><path d="M1.5 8h13M2.5 4.8h11M2.5 11.2h11"/></svg>
      ironvalesite.com
    </p>
  </div>

  <p class="address">2210 Cedar Lane Unit 400, Oak Harbor, Il 60099</p>

  <div class="side-band">
    <span class="band-name">IRONVALE<span class="band-suffix">INC</span></span>
  </div>
</section>

</body>
</html>
```